Otter Vale pipe restorations recruiting business card

We need a recruiting business card for our commercial pipe line company “Otter Vale” that reaches out to individuals looking for a job or who would be a great fit to our team. We want to include:
- Recognizing the candidates potential
—> You are amazing!
- Capture who we are (name, subtitle, tag line & our core values)
—> OTTER VALE, Pipe Restoration Solutions, INVESTIGATE | PLAN | DELIVER | , our values: Family, Integrity, Generosity, Faith, Humility, Communication, Collaboration, Innovation, Mission Minded, Positivity, Improvement, Fulfillment, Fun and Diversity
3. Call to action (apply at website/email this address/call this number to become apart of our team/family)
—> If you are interested in a career with a fully funded startup that is using technology and a new and innovative approach to the age old art of plumbing we are seeking team members who appreciate hard work and want to be part of a winning team!
—> send your resume to: recruiting@ottervale.example
4. Personal point of reference (let them know x [person handing out card writes their name] sent you! )
—> Let them know that _______________ sent you!
Call me if you have any questions _________________

Contact Information for Business Card

Front: Explaining who we are/core values
Back: recruitment explanation

Font styles to use
Serif
Sans Serif

```html
<!DOCTYPE html>
<html lang="en">
<head>
<meta charset="utf-8">
<title>Otter Vale – Recruiting Business Card</title>
<link rel="stylesheet" href="https://fonts.googleapis.com/css2?family=Roboto:wght@400;500;700&display=swap">
<style>
  :root {
    --backdrop: #5a5a5c;
    --ink: #111111;
    --paper: #ffffff;
    --card-black: #0d0d0d;
    --muted: #333333;
    --rule: #555555;
    --art-light: #f2f2f2;
    --art-dark: #cfcfcf;
  }
  * { box-sizing: border-box; margin: 0; padding: 0; }
  html, body {
    width: 1200px; height: 1124px; overflow: hidden;
    background: var(--backdrop);
    font-family: "Roboto", Arial, sans-serif;
  }
  .canvas { position: relative; width: 1200px; height: 1124px; }

  .card {
    position: absolute; left: 180px; width: 840px; height: 480px;
    box-shadow: 0 8px 22px rgba(0,0,0,.45);
  }

  /* Back: recruitment message */
  .card--back { top: 50px; background: var(--card-black); color: var(--paper); }
  .hero-art {
    position: absolute; left: 0; top: 110px; width: 360px; height: 330px;
    background: radial-gradient(ellipse at 45% 55%, var(--art-light) 0%, var(--art-dark) 70%, var(--card-black) 100%);
    border-radius: 40% 55% 45% 30%;
  }
  .pitch {
    position: absolute; left: 380px; top: 40px; width: 430px;
    text-align: center; font-size: 17px; line-height: 1.35;
  }
  .pitch__headline { font-weight: 700; font-size: 17px; margin-bottom: 34px; }
  .pitch__body { margin-bottom: 22px; }
  .pitch__rule { border-top: 1px solid var(--paper); margin: 0 0 70px; }
  .pitch__cta p { margin-bottom: 2px; }
  .blank { display: inline-block; border-bottom: 1px solid var(--paper); vertical-align: baseline; }

  /* Front: who we are */
  .card--front { top: 594px; background: var(--paper); color: var(--ink); }
  .company { position: absolute; left: 60px; top: 108px; width: 360px; }
  .company__name { font-weight: 500; font-size: 38px; line-height: 1.1; }
  .company__subtitle { font-size: 18px; color: var(--muted); margin-top: 8px; }
  .company__tagline { font-size: 18px; color: var(--muted); margin-top: 2px; }

  .divider { position: absolute; left: 448px; top: 70px; width: 1px; height: 210px; background: var(--rule); }
  .person { position: absolute; left: 490px; top: 72px; }
  .person__name { font-weight: 700; font-size: 30px; }
  .person__title { font-size: 22px; color: var(--muted); margin-top: 2px; }
  .person__address { font-size: 21px; color: var(--muted); margin-top: 22px; line-height: 1.2; }
  .contacts { list-style: none; margin-top: 18px; }
  .contacts li { display: flex; align-items: center; gap: 18px; font-size: 21px; color: var(--muted); margin-bottom: 6px; }
  .contacts svg { width: 18px; height: 18px; flex: none; }

  .values { position: absolute; left: 0; right: 0; top: 358px; text-align: center; }
  .values__tag {
    display: inline-block; background: var(--ink); color: var(--paper);
    font-weight: 500; font-size: 19px; letter-spacing: .5px;
    padding: 3px 26px; border-radius: 16px; margin-bottom: 6px;
  }
  .values__list { font-weight: 500; font-size: 18px; line-height: 1.3; padding: 0 20px; }
</style>
</head>
<body>
<main class="canvas">

  <section class="card card--back" aria-label="Card back: recruitment message">
    <div class="hero-art" role="img" aria-label="Large white animal head illustration on black"></div>
    <div class="pitch">
      <p class="pitch__headline">You are amazing!</p>
      <p class="pitch__body">If you are interested in a career with a fully funded startup that is using technology and a new and innovative approach to the age old art of plumbing we are seeking team members who appreciate hard work and want to be part of a winning team!</p>
      <div class="pitch__rule"></div>
      <div class="pitch__cta">
        <p>send your resume to: recruiting@ottervale.example</p>
        <p>Let them know that <span class="blank" style="width:110px"></span> sent you!</p>
        <p>Call me if you have any questions <span class="blank" style="width:120px"></span></p>
      </div>
    </div>
  </section>

  <section class="card card--front" aria-label="Card front: company and contact">
    <div class="company">
      <h1 class="company__name">Otter Vale</h1>
      <p class="company__subtitle">Pipe Restoration Solutions</p>
      <p class="company__tagline">Investigate | Plan | Deliver</p>
    </div>

    <div class="divider"></div>

    <div class="person">
      <div class="person__name">Marcus Reed</div>
      <div class="person__title">Manager</div>
      <div class="person__address">Your address, city<br>state, ZIP 0000</div>
      <ul class="contacts">
        <li><svg viewBox="0 0 24 24" aria-hidden="true"><path fill="#111" d="M6.6 10.8a15 15 0 0 0 6.6 6.6l2.2-2.2c.3-.3.7-.4 1-.2 1.1.4 2.3.6 3.6.6.6 0 1 .4 1 1V20c0 .6-.4 1-1 1A17 17 0 0 1 3 4c0-.6.4-1 1-1h3.5c.6 0 1 .4 1 1 0 1.3.2 2.5.6 3.6.1.3 0 .7-.2 1z"/></svg>123-456-2100</li>
        <li><svg viewBox="0 0 24 24" aria-hidden="true"><rect x="2" y="5" width="20" height="14" rx="1.5" fill="none" stroke="#111" stroke-width="2"/><path d="M2 6l10 7 10-7" fill="none" stroke="#111" stroke-width="2"/></svg>recruiting@ottervale.example</li>
        <li><svg viewBox="0 0 24 24" aria-hidden="true"><g fill="none" stroke="#111" stroke-width="2"><circle cx="12" cy="12" r="10"/><ellipse cx="12" cy="12" rx="4.5" ry="10"/><path d="M2 12h20M4 7h16M4 17h16"/></g></svg>www.yourwebsite.com</li>
      </ul>
    </div>

    <div class="values">
      <span class="values__tag">OUR VALUES</span>
      <p class="values__list">Family, Integrity, Generosity, Faith, Humility, Communication, Collaboration, Innovation<br>Mission Minded, Positivity, Improvement, Fulfillment, Fun and Diversity</p>
    </div>
  </section>

</main>
</body>
</html>
```